Wholesale e-commerce website re-design

We are a wholesaler of African-made and African-themed products, and we're looking to update the look and feel of our website www.terramarketgoods.com to improve user experience. We'd like to have a cleaner homepage that keeps the product category menus (but simplifies them), allows certain products to be featured, and has a simple CTA box (something like "Login" for existing wholesale customers or "Start a Business" for new customers). The layout might be something along the lines of http://www.pinewillowwares.com/ except with a shopping cart featured at the top right. Our colors tend to be earth-toned, but the current color palate looks dated. Also see our blog.terramarketgoods.com page for themes and color ideas that are maybe more up-to-date. On our product pages, we want to feature the products more prominently and have simpler, cleaner Buy or Add buttons.

Other reference sites for inspiration: vastherbalcrate.com, cozykitchenry.com, http://www.pinewillowwares.com, http://mbelatraders.com/ http://orunesa.com/

Reason: We like many of the designs that have been submitted so far, but need more time to make our final choice.

Target Market(s)

Small wholesale customers, most have a small business or home-based business. Also some retail, so an option for retail customers to click at the top to see retail pricing would be nice

Industry/Entity Type

Wholesale

Number of Pages Required

3 page

Font styles to use
Sans Serif

Requirements
Must have
• Clean, clear design that highlights products and reduces friction to customer purchase. Should include one homepage, one product page, and one shopping cart page design. Works with all browser types and be mobile-friendly.
Nice to have
• Other color schemes that would look good with our logo (maybe different from colors chosen below).
Should not have
• Splash pages with special effects, Adobe flash, elements that slow down page load times or that only work well in certain browsers.

```html
<!DOCTYPE html>
<html lang="en">
<head>
<meta charset="utf-8">
<title>Terra Market — Wholesale</title>
<link href="https://fonts.googleapis.com/css2?family=Questrial&family=Nunito+Sans:wght@700;800&display=swap" rel="stylesheet">
<style>
:root{
  --brand:#c8433a;
  --brand-dark:#b53a31;
  --ink:#2a2a2a;
  --muted:#555;
  --line:#d6d6d6;
  --grey-btn:#d4d4d4;
  --white:#fff;
}
*{box-sizing:border-box;margin:0;padding:0}
html,body{width:1200px;height:1174px;overflow:hidden}
body{font-family:"Questrial",sans-serif;color:var(--ink);background:var(--white);position:relative}
a{color:inherit;text-decoration:none}
ul{list-style:none}
.heading{font-family:"Nunito Sans",sans-serif;font-weight:800}

.topbar{position:absolute;left:0;top:0;width:1189px;height:43px;background:var(--brand);color:var(--white);display:flex;align-items:center;padding:0 100px 0 103px;justify-content:space-between}
.topbar .phone{font-family:"Nunito Sans",sans-serif;font-weight:800;font-size:17px;display:flex;align-items:center;gap:9px}
.topbar .utility{display:flex;align-items:center;font-size:14px}
.topbar .utility li{padding:0 17px;border-left:1px solid rgba(255,255,255,.8);display:flex;align-items:center;gap:7px;line-height:14px}
.topbar .utility li:first-child{border-left:0}
.topbar .utility li:last-child{padding-right:0}

.logo{position:absolute;left:104px;top:58px;width:104px;height:112px;display:flex;flex-direction:column;align-items:center;justify-content:center}
.logo-name{font-family:"Nunito Sans",sans-serif;font-weight:800;font-size:19px;color:var(--ink);text-align:center;line-height:1.1}
.logo-dot{width:14px;height:14px;border-radius:50%;background:var(--brand);margin-bottom:8px}

.search{position:absolute;left:502px;top:60px;width:202px;height:31px;border:1px solid var(--line);display:flex;align-items:center;justify-content:space-between;padding:0 8px 0 11px;font-size:14px;color:var(--muted)}
.social-top{position:absolute;left:736px;top:60px;display:flex;gap:9px}
.circle{width:31px;height:31px;border:1.5px solid var(--brand);border-radius:50%;display:block}
.support{position:absolute;left:911px;top:60px;width:190px;height:31px;background:var(--grey-btn);border-radius:2px;display:flex;align-items:center;justify-content:center;gap:6px;font-size:13px;color:var(--ink)}

.mainnav{position:absolute;left:241px;top:143px;width:860px;display:flex;justify-content:space-between;font-size:17px}
.mainnav .active{color:var(--brand)}

.hero{position:absolute;left:99px;top:178px;width:690px;height:472px;background:linear-gradient(135deg,#6b5a4a 0%,#9b8a76 35%,#4a3c30 65%,#2d2520 100%)}
.hero-caption{position:absolute;left:0;bottom:0;width:100%;height:47px;background:rgba(0,0,0,.55);display:flex;align-items:center;justify-content:space-between;padding:0 15px 0 12px;color:var(--white);font-family:"Nunito Sans",sans-serif;font-weight:800;font-size:18px}
.dots{display:flex;gap:5px}
.dots span{width:10px;height:10px;border-radius:50%;background:var(--brand);border:2px solid var(--white)}
.dots span:first-child{background:#ddd}

.cta{position:absolute;left:800px;top:178px;width:300px;height:472px;background:var(--brand);color:var(--white);text-align:center;padding-top:8px}
.cta h2{font-size:16px;line-height:21px}
.cta-photo{margin:10px auto 0;width:284px;height:224px;border:3px solid #e6dcd0;background:linear-gradient(180deg,#d8cfc3,#c7b9a6 60%,#e4ddd3)}
.cta p{font-size:13.5px;line-height:16px;padding:0 8px}
.cta .lead{margin-top:14px}
.cta .body1{margin-top:11px}
.cta .body2{margin-top:9px}
.cta-btn{display:inline-block;margin-top:18px;width:182px;height:31px;line-height:31px;background:var(--white);color:var(--brand);border-radius:3px;font-family:"Nunito Sans",sans-serif;font-weight:800;font-size:16px}

.features{position:absolute;top:698px;left:0;width:1200px}
.feature{position:absolute;width:266px;height:103px;border:1px solid var(--line);display:flex;align-items:center;padding-left:14px;gap:14px;font-size:14px;color:var(--muted)}
.feature strong{display:block;font-weight:400;font-size:14.5px;color:#333;margin-bottom:4px;letter-spacing:.2px}

.footer{position:absolute;left:0;top:842px;width:1200px;height:288px;background:linear-gradient(180deg,#f4f6f8 0%,#e8ecf0 55%,#dfe4e9 100%)}
.fcol{position:absolute;top:34px}
.fcol h3{font-size:15.5px;padding-bottom:10px;border-bottom:1px solid #d0d0d0;margin-bottom:12px;color:#222}
.fcol li{font-size:14px;color:#444;height:24.5px;display:flex;align-items:center;gap:8px}
.fcol li::before{content:"";width:5px;height:5px;border-right:1.5px solid #333;border-top:1.5px solid #333;transform:rotate(45deg)}
.newsletter p{font-size:12.5px;color:#555;line-height:17px;margin-top:-2px}
.subscribe{display:flex;margin-top:14px;height:32px}
.subscribe span{flex:1;border:1px solid #ccc;background:var(--white);font-size:11.5px;color:#777;display:flex;align-items:center;padding-left:8px}
.subscribe b{width:82px;background:var(--brand);color:var(--white);font-weight:400;font-size:13px;display:flex;align-items:center;justify-content:center}
.follow{margin-top:24px}
.social-foot{display:flex;gap:9px;margin-left:1px}
.payments{display:flex;gap:7px}
.payments span{width:34px;height:21px;border:1px solid #ccc;background:var(--white);border-radius:2px}
.payments span:nth-child(2){background:#e7e7e7}
.payments span:nth-child(4){background:#e7e7e7}

.copyright{position:absolute;left:0;top:1130px;width:1200px;height:44px;background:var(--brand);color:var(--white);font-size:14px;display:flex;align-items:center;justify-content:center}
</style>
</head>
<body>

<header class="topbar">
  <div class="phone">
    <svg width="17" height="17" viewBox="0 0 24 24" fill="#fff"><path d="M6.6 10.8c1.4 2.8 3.8 5.1 6.6 6.6l2.2-2.2c.3-.3.7-.4 1-.2 1.1.4 2.3.6 3.6.6.6 0 1 .4 1 1V20c0 .6-.4 1-1 1C10.6 21 3 13.4 3 4c0-.6.4-1 1-1h3.5c.6 0 1 .4 1 1 0 1.3.2 2.5.6 3.6.1.3 0 .7-.2 1z"/></svg>
    +123 456 7890
  </div>
  <ul class="utility">
    <li>
      <svg width="26" height="20" viewBox="0 0 26 20" fill="none" stroke="#fff" stroke-width="1.6"><path d="M1 2h4l3 11h13l3-8H7"/><circle cx="10" cy="17" r="1.6"/><circle cx="19" cy="17" r="1.6"/></svg>
      View Cart (0)
    </li>
    <li>Checkout</li>
    <li>My Cart</li>
    <li>My Wishlist</li>
    <li>
      <svg width="10" height="13" viewBox="0 0 10 13" fill="#fff"><rect x="0" y="6" width="10" height="7" rx="1"/><path d="M2 6V4a3 3 0 0 1 6 0" fill="none" stroke="#fff" stroke-width="1.6"/></svg>
      Log In
    </li>
    <li>
      <svg width="14" height="14" viewBox="0 0 14 14" fill="#fff"><circle cx="7" cy="4" r="3.2"/><path d="M1 14c0-3.5 2.7-5.5 6-5.5s6 2 6 5.5z"/></svg>
      My Account
    </li>
  </ul>
</header>

<a class="logo" href="#">
  <span class="logo-dot"></span>
  <span class="logo-name">TERRA<br>MARKET</span>
</a>

<div class="search">
  <span>Search...</span>
  <svg width="14" height="14" viewBox="0 0 14 14" fill="none" stroke="#c8433a" stroke-width="2"><circle cx="6" cy="6" r="4.3"/><path d="M9.2 9.2L13 13"/></svg>
</div>

<div class="social-top" aria-label="Social links">
  <span class="circle"></span><span class="circle"></span><span class="circle"></span><span class="circle"></span>
</div>

<a class="support" href="#">
  <svg width="13" height="13" viewBox="0 0 14 14" fill="#c8433a"><circle cx="7" cy="4" r="3.2"/><path d="M1 14c0-3.5 2.7-5.5 6-5.5s6 2 6 5.5z"/></svg>
  Support Online - Chat Now
</a>

<nav class="mainnav">
  <a class="active" href="#">Home</a>
  <a href="#">All Categories</a>
  <a href="#">Products</a>
  <a href="#">Sale</a>
  <a href="#">New Items</a>
  <a href="#">Other Accessories</a>
  <a href="#">Blog</a>
  <a href="#">About Us</a>
  <a href="#">Contact Us</a>
</nav>

<section class="hero" role="img" aria-label="Photo of shea butter in a bowl, a patterned tagine with argan nuts and a bottle of oil beside white flowers">
  <div class="hero-caption">
    <span>We are a wholesaler of African-made and African-themed products</span>
    <div class="dots"><span></span><span></span><span></span><span></span></div>
  </div>
</section>

<aside class="cta">
  <h2 class="heading">Start your African business today!<br>Only $49.00 &amp; FREE Shipping</h2>
  <div class="cta-photo" role="img" aria-label="Photo of the business start-up kit: assorted soaps, butters and small jars"></div>
  <p class="lead">Get the Easy Business Start-Up Kit Today!</p>
  <p class="body1">Once you get the Start-Up Kit, you can immediately get new customers &amp; start selling products.</p>
  <p class="body2">Now is the best time to start a business &amp; earn extra money. Click here for more details.</p>
  <a class="cta-btn" href="#">Start Business Today</a>
</aside>

<section class="features">
  <div class="feature" style="left:165px">
    <svg width="44" height="36" viewBox="0 0 44 36" fill="#333"><rect x="14" y="4" width="29" height="22" rx="2"/><path d="M13 11H6l-5 7v8h12z"/><circle cx="9" cy="29" r="4.5" stroke="#fff" stroke-width="2"/><circle cx="34" cy="29" r="4.5" stroke="#fff" stroke-width="2"/></svg>
    <div><strong>FREE DELIVERY WORLDWIDE</strong>On order over $ 400.00</div>
  </div>
  <div class="feature" style="left:467px">
    <svg width="44" height="40" viewBox="0 0 44 40" fill="#333"><rect x="2" y="12" width="40" height="8"/><rect x="5" y="21" width="34" height="18"/><rect x="19" y="12" width="6" height="27" fill="#fff"/><path d="M22 12c-4-8-12-10-12-4s8 4 12 4c4 0 12 2 12-4s-8-4-12 4z" fill="none" stroke="#333" stroke-width="3"/></svg>
    <div><strong>DISCOUNT ON ORDER GIFT</strong>At vero eos accusamus iusto</div>
  </div>
  <div class="feature" style="left:763px">
    <svg width="44" height="46" viewBox="0 0 44 46" fill="#333"><circle cx="20" cy="13" r="9"/><path d="M9 13a11 11 0 0 1 22 0" fill="none" stroke="#333" stroke-width="2.5"/><path d="M2 44c0-10 8-16 18-16 6 0 10 2 13 5v11z"/><circle cx="34" cy="37" r="7" stroke="#fff" stroke-width="2"/><path d="M31 34l6 6M37 34l-6 6" stroke="#fff" stroke-width="2"/></svg>
    <div><strong>CUSTOMER SUPPORT</strong>We Are Here For You!</div>
  </div>
</section>

<footer class="footer" role="contentinfo">
  <div class="fcol newsletter" style="left:100px;width:245px">
    <h3 class="heading">Newsletter Sign-up</h3>
    <p>Lorem ipsum dolor sit amet, consecte lorem adipiscing elit sed diamr</p>
    <div class="subscribe"><span>Enter your Email Address</span><b>SUBSCRIBE</b></div>
    <h3 class="heading follow">Follow Us On</h3>
    <div class="social-foot"><span class="circle"></span><span class="circle"></span><span class="circle"></span><span class="circle"></span></div>
  </div>

  <div class="fcol" style="left:430px;width:114px">
    <h3 class="heading">Quick Links</h3>
    <ul><li>Home</li><li>All Categories</li><li>Products</li><li>Sale</li><li>New Items</li><li>Other Accessories</li><li>About Us</li><li>Contact Us</li></ul>
  </div>

  <div class="fcol" style="left:632px;width:200px">
    <h3 class="heading">More About Terra Market</h3>
    <ul><li>About Terra Market</li><li>How We Help Africa</li><li>African Proverbs</li><li>Free Articles</li><li>How Can We Improve?</li></ul>
    <h3 class="heading" style="border:0;margin:8px 0 0;padding-bottom:8px">Payments Options</h3>
    <div class="payments" aria-label="Accepted payment methods"><span></span><span></span><span></span><span></span><span></span></div>
  </div>

  <div class="fcol" style="left:913px;width:183px">
    <h3 class="heading">Shipping &amp; Returns</h3>
    <ul><li>Standard Return Policy</li><li>Shipping Policy</li><li>Delivery Policies</li></ul>
    <h3 class="heading" style="margin-top:40px">Make Money With Us</h3>
    <ul><li>Lorem&nbsp; Ispum is the dummy</li><li>Lorem Ispum</li></ul>
  </div>
</footer>

<div class="copyright">Copyright © 2017 Terra Market. All Rights Reserved.</div>

</body>
</html>
```